依頼詳細
【制作希望パターン】
①高級感のあるページ
②シンプルかつあたたかみのあるページ
③スタイリッシュなページ
上記3パターンのいずれかのイメージに合わせて制作してください。

【カラー】
ベースカラー:サーモンピンク(落ち着いたピンク色)
ポイントカラー:パープル?
ベースカラーは指定の色味でお願いします。
ポイントカラーはデザインに合わせてご提案ください。

【要素】
①グローバルナビ
・診察について
・施設紹介
・ドクター紹介
・入院案内
・ソフロロジー分娩法
・産後ケア&サポート

②ナビ外に常に表示するメニュー
・教室案内
・予約診察
※表示方法の参考イメージ
http://www.korinomi-iin.example/about/

③トップコンテンツ
・病院の基本理念(ダミーテキストで構いません)
・新着お知らせ(ダミーテキストで構いません)
・お産関連コンテンツのカード型メニュー4つ(横並びイメージ)
┗妊婦検診/マザークラス・マタニティヨーガ/ソフロロジー分娩/産後サポート

④使用画像
メインイメージ→施設外観写真/その他産婦人科に見合うイメージ
※写真スライダーで表示予定
※施設外観写真は添付の画像を使用してください
背景イメージ→新着お知らせの横に部屋写真を使用(ダミーで構いません)
※表示の参考イメージ
http://www.tobuhira-clinic.example/
サイトURL
http://www.miwaku-ladies.example/info.html
ページ数
1ページ
希望イメージ
シンプル 複雑
単色 カラフル
暗い 明るい
日常 高級
遊び心 厳粛
未来的 伝統的
女性的 男性的
希望する色
赤系
納品ファイル
• 高解像度JPG (.jpg)
• フォトショップ形式 (.psd)
補足説明
今回のコンペで当選された方には、中ページ(PC・スマホ)のデザイン制作を追加でお願いする可能性がございます。
報酬金額2万円程度を想定しておりますので、その際はお力添えお願いいたします。
ご提案について

現時点で3件ほどご提案をいただきましたが、デザインのご提案ではなく
ご自身・自社のアピールのみをテキストで提案欄に記入されているため
ワークモア規約により削除されております。
デザインコンペの案件ですので、お手数ですが依頼詳細に合わせてデザインのご提案を
いただけますと幸いです。
今回の案件に限らずデザインサポートをいただける方はこちらに提案ではなくメッセージにてご連絡くださいませ。

皆様からのご提案お待ちしております。
■ 選んだ理由

シンプルでレスポンシブでもストレスのないレイアウト・デザインに
弊社の提示した要素を無理なく盛り込んでいただいたkuruto-works様の
デザイン案で決定させていただきました。

■ 提案者全員のお礼・コメント

この度は多くのご提案をいただき、ありがとうございました。
今後とも、弊社にお力添えいただけますと幸いです。

```html
<!DOCTYPE html>
<html lang="ja">
<head>
<meta charset="utf-8">
<title>美和久レディースクリニック</title>
<link href="https://fonts.googleapis.com/css2?family=Noto+Sans+JP:wght@400;500;700&family=Noto+Serif+JP:wght@500&display=swap" rel="stylesheet">
<style>
:root{
  --salmon:#e9a3a6;
  --salmon-deep:#d98589;
  --salmon-pale:#fbeeee;
  --salmon-tint:#f6dcdc;
  --cream:#fdf7f3;
  --purple:#6f5a9a;
  --text:#5a4a4a;
  --muted:#9a8a8a;
  --line:#ecd6d3;
  --gold:#c9a77a;
}
*{margin:0;padding:0;box-sizing:border-box}
html,body{width:686px;height:1200px;overflow:hidden;background:#fff}
body{font-family:"Noto Sans JP",sans-serif;color:var(--text);font-size:9px;position:relative}
a{color:inherit;text-decoration:none}
.canvas{position:relative;width:686px;height:1200px}

.site-header{position:absolute;top:0;left:0;width:686px;height:56px}
.brand{display:flex;align-items:center;gap:6px}
.site-header .brand{position:absolute;left:22px;top:14px}
.brand-dot{width:10px;height:10px;background:var(--purple);border-radius:50%;flex:none}
.brand-name{font-size:10px;font-weight:500;color:var(--purple);line-height:1.2;white-space:nowrap}
.global-nav{position:absolute;left:262px;top:18px;display:flex}
.global-nav a{display:block;font-size:8px;color:var(--text);padding:5px 8px;border-left:1px solid var(--line);white-space:nowrap}
.global-nav a:first-child{color:#fff;background:var(--salmon);border-left:none}

.hero{position:absolute;top:56px;left:0;width:686px;height:276px;background:linear-gradient(90deg,#fff 0%,var(--cream) 100%)}
.hero-photo{position:absolute;left:0;top:0;width:370px;height:276px;background:linear-gradient(135deg,#f4e6e0 0%,#ead3cb 50%,#f7efe9 100%)}
.hero-copy{position:absolute;left:386px;top:105px;width:192px}
.hero-title{font-family:"Noto Serif JP",serif;font-size:11px;font-weight:500;color:var(--text);margin-bottom:14px;white-space:nowrap}
.hero-text{font-size:7.5px;line-height:2.1;color:var(--text);white-space:nowrap}
.side-menu{position:absolute;right:12px;top:84px;width:92px;display:flex;flex-direction:column;gap:6px}
.side-menu a{display:block;text-align:center;font-size:8.5px;color:#fff;background:var(--salmon);padding:6px 0;border-radius:2px}
.side-menu a.reserve{background:var(--salmon-deep)}
.side-phone{text-align:center;font-size:11px;font-weight:700;color:var(--salmon-deep);background:#fff;border:1px solid var(--salmon);padding:4px 0;border-radius:2px}

.news-band{position:absolute;top:343px;left:0;width:686px;height:250px;background:var(--salmon-pale)}
.news{position:absolute;left:46px;top:18px;width:300px}
.news-head{display:flex;align-items:center;gap:8px;margin-bottom:14px}
.news-title{font-size:11px;color:var(--salmon-deep);font-weight:500}
.news-tag{font-size:7px;color:#fff;background:var(--salmon);padding:1px 6px;border-radius:7px}
.news-list{list-style:none}
.news-list li{display:flex;gap:14px;font-size:8px;padding:6px 0;border-bottom:1px dotted var(--line)}
.news-list .date{color:var(--salmon-deep)}
.room-photo{position:absolute;left:354px;top:0;width:332px;height:250px;background:linear-gradient(160deg,#fbf6f3 0%,#e9e2de 60%,#d8d3d0 100%)}

.deco-line{position:absolute;top:604px;left:0;width:686px;height:1px;background:var(--line)}
.cards{position:absolute;top:640px;left:36px;width:614px;display:flex;gap:8px}
.card{flex:1;height:92px;border:1px solid var(--gold);border-radius:3px;background:#fff;display:flex;align-items:stretch;overflow:hidden;color:var(--text)}
.card-label{width:68px;flex:none;display:flex;align-items:center;justify-content:center;text-align:center;font-size:7.5px;line-height:1.6;color:var(--text);white-space:nowrap}
.card-photo{flex:1;background:linear-gradient(135deg,#f7e3e1,#ecc9c8)}
.card:nth-child(2) .card-photo{background:linear-gradient(135deg,#f1e9e3,#dccfc6)}
.card:nth-child(3) .card-photo{background:linear-gradient(135deg,#f8d6d8,#eab3b6)}
.card:nth-child(4) .card-photo{background:linear-gradient(135deg,#f5ebe6,#e4d2ca)}

.hours{position:absolute;left:26px;top:808px;width:306px;height:136px;background:var(--salmon-pale);border:1px solid var(--line);border-radius:4px;padding:12px 14px}
.hours-title{font-size:10px;color:var(--salmon-deep);font-weight:500;margin-bottom:8px}
.hours table{width:100%;border-collapse:collapse;font-size:8px}
.hours th,.hours td{text-align:center;padding:6px 0;border-bottom:1px dotted var(--salmon)}
.hours th{font-weight:400;color:var(--text)}
.hours td.time{text-align:left;color:var(--salmon-deep);white-space:nowrap}
.hours td svg{vertical-align:middle}
.hours-note{font-size:6.5px;text-align:right;color:var(--muted);margin-top:6px}

.access{position:absolute;left:344px;top:808px;width:318px}
.map{width:318px;height:136px;background:linear-gradient(135deg,#efeeec,#e2e0dc)}
.address{font-size:7.5px;margin-top:10px;line-height:1.7}
.access-notes{font-size:6.5px;color:var(--muted);line-height:1.7;margin-top:4px}

.site-footer{position:absolute;top:1006px;left:0;width:686px;height:194px;background:var(--salmon-tint)}
.footer-brand{position:absolute;left:22px;top:30px}
.footer-cols{position:absolute;left:354px;top:22px;display:flex;gap:34px}
.footer-cols ul{list-style:none}
.footer-cols li{font-size:7px;color:var(--text);line-height:2.1;white-space:nowrap}
.footer-cols li::before{content:"› ";color:var(--salmon-deep)}
.copyright{position:absolute;bottom:0;left:0;width:686px;height:26px;background:var(--salmon);color:#fff;font-size:7px;text-align:center;line-height:26px;letter-spacing:.05em}
</style>
</head>
<body>
<div class="canvas">

<header class="site-header">
  <div class="brand">
    <span class="brand-dot"></span>
    <span class="brand-name">MIWAKU LADIES CLINIC<br>美和久レディースクリニック</span>
  </div>
  <nav class="global-nav">
    <a href="#">診察について</a>
    <a href="#">施設紹介</a>
    <a href="#">ドクター紹介</a>
    <a href="#">入院案内</a>
    <a href="#">ソフロロジー分娩</a>
    <a href="#">産後ケア&amp;サポート</a>
  </nav>
</header>

<section class="hero">
  <div class="hero-photo" role="img" aria-label="赤ちゃんを抱く母親のメイン写真"></div>
  <div class="hero-copy">
    <h1 class="hero-title">新しい"いのち"の誕生を手助けします。</h1>
    <p class="hero-text">おかあさんと赤ちゃんの笑顔を大切に<br>おひとりおひとりに寄り添い安心して出産<br>を迎えていただけるよう<br>スタッフ一同、真心を込めてサポートします。<br>これからも安心できる医療を提供いたします。</p>
  </div>
  <div class="side-menu">
    <a href="#">教室案内</a>
    <a href="#" class="reserve">予約診察</a>
    <div class="side-phone">092-000-4817</div>
  </div>
</section>

<section class="news-band">
  <div class="news">
    <div class="news-head"><h2 class="news-title">お知らせ</h2><span class="news-tag">一覧を見る</span></div>
    <ul class="news-list">
      <li><span class="date">2016.4.30</span><span>ホームページをリニューアルしました！</span></li>
      <li><span class="date">2016.4.30</span><span>ダミーテキストダミーテキスト</span></li>
      <li><span class="date">2016.4.30</span><span>ダミーテキストダミーテキスト</span></li>
      <li><span class="date">2016.4.30</span><span>ダミーテキストダミーテキスト</span></li>
    </ul>
  </div>
  <div class="room-photo" role="img" aria-label="明るい病室とベッドの写真"></div>
</section>

<div class="deco-line"></div>

<section class="cards">
  <a class="card" href="#"><span class="card-label">妊婦検診</span><span class="card-photo" role="img" aria-label="妊婦検診の写真"></span></a>
  <a class="card" href="#"><span class="card-label">マザークラス<br>マタニティヨーガ</span><span class="card-photo" role="img" aria-label="マタニティヨーガの写真"></span></a>
  <a class="card" href="#"><span class="card-label">ソフロロジー<br>分娩</span><span class="card-photo" role="img" aria-label="新生児の写真"></span></a>
  <a class="card" href="#"><span class="card-label">産後サポート</span><span class="card-photo" role="img" aria-label="母子の産後ケアの写真"></span></a>
</section>

<section class="hours">
  <h2 class="hours-title">診療時間</h2>
  <table>
    <tr><th></th><th>月</th><th>火</th><th>水</th><th>木</th><th>金</th><th>土</th><th>日</th></tr>
    <tr><td class="time">9:00〜12:30</td>
      <td><svg width="8" height="8"><circle cx="4" cy="4" r="3.2" fill="none" stroke="#d98589"/></svg></td>
      <td><svg width="8" height="8"><circle cx="4" cy="4" r="3.2" fill="none" stroke="#d98589"/></svg></td>
      <td><svg width="8" height="8"><circle cx="4" cy="4" r="3.2" fill="none" stroke="#d98589"/></svg></td>
      <td><svg width="8" height="8"><circle cx="4" cy="4" r="3.2" fill="none" stroke="#d98589"/></svg></td>
      <td><svg width="8" height="8"><circle cx="4" cy="4" r="3.2" fill="none" stroke="#d98589"/></svg></td>
      <td><svg width="8" height="8"><circle cx="4" cy="4" r="3.2" fill="none" stroke="#d98589"/></svg></td>
      <td></td></tr>
    <tr><td class="time">14:30〜17:30</td>
      <td><svg width="8" height="8"><circle cx="4" cy="4" r="3.2" fill="none" stroke="#d98589"/></svg></td>
      <td><svg width="8" height="8"><circle cx="4" cy="4" r="3.2" fill="none" stroke="#d98589"/></svg></td>
      <td><svg width="8" height="8"><circle cx="4" cy="4" r="3.2" fill="none" stroke="#d98589"/></svg></td>
      <td><svg width="8" height="8"><circle cx="4" cy="4" r="3.2" fill="none" stroke="#d98589"/></svg></td>
      <td><svg width="8" height="8"><circle cx="4" cy="4" r="3.2" fill="none" stroke="#d98589"/></svg></td>
      <td></td><td></td></tr>
  </table>
  <p class="hours-note">※休診日は日曜日・祝日です</p>
</section>

<section class="access">
  <div class="map" role="img" aria-label="クリニック周辺の地図"></div>
  <p class="address">住所：〒810-0000 福岡県架空市若葉町1-2-3</p>
  <p class="access-notes">■ お車でお越しの方：駐車場を完備しております。<br>■ 電車でお越しの方：最寄駅より徒歩5分です。</p>
</section>

<footer class="site-footer">
  <div class="brand footer-brand">
    <span class="brand-dot"></span>
    <span class="brand-name">MIWAKU LADIES CLINIC<br>美和久レディースクリニック</span>
  </div>
  <div class="footer-cols">
    <ul><li>診察について</li><li>施設紹介</li><li>ドクター紹介</li><li>入院案内</li></ul>
    <ul><li>ソフロロジー分娩</li><li>産後ケア</li><li>教室案内</li><li>予約診察</li></ul>
    <ul><li>お知らせ</li><li>アクセス</li><li>よくある質問</li><li>お問い合わせ</li></ul>
  </div>
  <p class="copyright">Copyright © MIWAKU LADIES CLINIC All Rights Reserved.</p>
</footer>

</div>
</body>
</html>
```